Business Card for Bright Meadow Lawn & Landscape

Double Sided Card Design - I think one side of the card should be cleaner, with logo, contact info, and "Complete Residential & Commercial Landscape Services", and on the other side it should list the services we offer:

- Lawn Care & Mowing
- Hedge & Shrub Trimming
- Leaf Removal & Clean Up
- Aeration & Sod
- Mulch & Rock Installations
- Landscape Installations & Renovations
- Commercial Snow Removal

Please make it clean and very professional... don't want it too be too busy, but want to tell them what we do.

Target Market(s)

Residential and Commercial

Industry/Entity Type

Landscape

Contact Information for Business Card

Fully Insured
Tom Berrigan
410-555-0198
Tberrigan07@mailbox-example.com

Requirements
Must have
• Double Sided, Cleaner on one side, more information and text on the other side.

```html
<!DOCTYPE html>
<html lang="en">
<head>
<meta charset="UTF-8">
<title>Bright Meadow Lawn &amp; Landscape — Business Card</title>
<link href="https://fonts.googleapis.com/css2?family=Cinzel:wght@400;500;600&family=Lato:wght@400;700&display=swap" rel="stylesheet">
<style>
  :root {
    --grass: #86b400;
    --grass-pale: #cfe39a;
    --charcoal: #242425;
    --paper: #ffffff;
    --ink: #2a2a2a;
    --backdrop: #e9e9e7;
  }
  * { margin: 0; padding: 0; box-sizing: border-box; }
  html, body { width: 1200px; height: 900px; overflow: hidden; }
  body {
    position: relative;
    background: var(--backdrop);
    font-family: "Lato", Arial, sans-serif;
  }
  .card {
    position: absolute;
    overflow: hidden;
    box-shadow: 0 6px 18px rgba(0,0,0,0.18);
  }

  /* Services side */
  .card-services {
    left: 177px; top: 73px; width: 589px; height: 365px;
    background: var(--paper);
  }
  .side-band { position: absolute; left: 0; top: 0; width: 340px; height: 365px; }
  .grass-illustration {
    position: absolute; left: 50px; top: 75px; width: 285px; height: 290px;
    background: linear-gradient(200deg, rgba(134,180,0,0.15) 0%, rgba(134,180,0,0.55) 100%);
  }
  .contact-block {
    position: absolute; right: 36px; top: 44px;
    text-align: right; color: var(--ink);
  }
  .holder-name {
    font-family: "Cinzel", Georgia, serif; font-weight: 500;
    font-size: 26px; color: var(--grass); letter-spacing: 0.5px;
    line-height: 34px; margin-bottom: 11px;
  }
  .contact-line {
    display: flex; justify-content: flex-end; align-items: center;
    gap: 5px; font-size: 16px; line-height: 22px;
  }
  .contact-line svg { width: 13px; height: 13px; fill: var(--grass); }
  .services-title {
    margin-top: 32px; font-size: 16px; font-weight: 400; color: var(--grass);
    text-transform: uppercase; letter-spacing: 0.3px; line-height: 22px;
  }
  .services-list { list-style: none; margin-top: 2px; }
  .services-list li {
    font-size: 14.5px; line-height: 22px;
    display: flex; justify-content: flex-end; align-items: center; gap: 6px;
  }
  .services-list li::after {
    content: ""; width: 6px; height: 6px; border-radius: 50%;
    background: var(--grass);
  }

  /* Brand side */
  .card-brand {
    left: 388px; top: 505px; width: 567px; height: 352px;
    background: var(--charcoal); color: var(--paper); text-align: center;
  }
  .brand-dot {
    position: absolute; left: 236px; top: 50px;
    width: 96px; height: 96px; border-radius: 50%;
    background: var(--grass);
  }
  .brand-name {
    position: absolute; left: 0; right: 0; top: 176px;
    font-family: "Cinzel", Georgia, serif; font-weight: 600;
    font-size: 35px; letter-spacing: 0.5px; line-height: 1;
    color: var(--grass);
  }
  .brand-descriptor {
    position: absolute; left: 0; right: 0; top: 212px;
    font-family: "Cinzel", Georgia, serif; font-weight: 400;
    font-size: 19px; letter-spacing: 3.5px; line-height: 1;
    color: var(--paper);
  }
  .insured {
    position: absolute; left: 0; right: 0; top: 248px;
    font-size: 13.5px; letter-spacing: 2.5px; text-transform: uppercase;
  }
  .tagline-band {
    position: absolute; left: 0; right: 0; bottom: 0; height: 65px;
    background: var(--grass);
    display: flex; align-items: center; justify-content: center;
    font-family: "Cinzel", Georgia, serif; font-weight: 600;
    font-size: 15px; letter-spacing: 0.6px;
  }
</style>
</head>
<body>

<section class="card card-services">
  <svg class="side-band" viewBox="0 0 340 365" aria-hidden="true">
    <path d="M0 0 H215 C140 60 70 180 45 365 H0 Z" fill="var(--grass)"/>
  </svg>
  <div class="grass-illustration" role="img" aria-label="Stylised green grass blades illustration"></div>

  <div class="contact-block">
    <h1 class="holder-name">Tom Berrigan</h1>
    <p class="contact-line">410-555-0198
      <svg viewBox="0 0 24 24" aria-hidden="true"><path d="M6.6 10.8a15 15 0 0 0 6.6 6.6l2.2-2.2a1 1 0 0 1 1-.25 11.4 11.4 0 0 0 3.6.57 1 1 0 0 1 1 1V20a1 1 0 0 1-1 1A17 17 0 0 1 3 4a1 1 0 0 1 1-1h3.5a1 1 0 0 1 1 1c0 1.25.2 2.45.57 3.57a1 1 0 0 1-.25 1z"/></svg>
    </p>
    <p class="contact-line">Tberrigan07@mailbox-example.com
      <svg viewBox="0 0 24 24" aria-hidden="true"><path d="M2 5h20v14H2z M3.5 6.5 12 13l8.5-6.5" fill="var(--grass)" stroke="#fff" stroke-width="1.6"/></svg>
    </p>
    <h2 class="services-title">Services We Offer:</h2>
    <ul class="services-list">
      <li>Lawn Care &amp; Mowing</li>
      <li>Hedge &amp; Shrub Trimming</li>
      <li>Leaf Removal &amp; Clean Up</li>
      <li>Aeration &amp; Sod</li>
      <li>Mulch &amp; Rock Installations</li>
      <li>Landscape Installations &amp; Renovations</li>
      <li>Commercial Snow Removal</li>
    </ul>
  </div>
</section>

<section class="card card-brand">
  <span class="brand-dot" aria-hidden="true"></span>
  <h2 class="brand-name">Bright Meadow</h2>
  <p class="brand-descriptor">Lawn &amp; Landscape</p>
  <p class="insured">Fully Insured</p>
  <div class="tagline-band">Complete Residential &amp; Commercial Landscape Services</div>
</section>

</body>
</html>
```